THE HEADLAND AT TALL PINE HUDSON RIVER WATERFRONT LAND

crisp clear business cards on wood stock or thick paper with large font with a river otter logo, PERSONAL INFO ON ONE SIDE, PROJECT INFO ON THE OTHER SIDE
Updates

I don’t have a logo. Just thought that a photo of a river otter would look appealing.

Target Market(s)

Buyers and realtors

Industry/Entity Type

Real Estate Development

Contact Information for Business Card

MARTIN KOWALCZYK
607-318-5942 (Call or Text)
STONE MEADOW LLC PRINCIPAL

RQVWFIELD@NORVAMAIL.NET

Font styles to use
Sans Serif

Colors
fbfdfe
0792cd
00a990
fbed22
ec1f27

Requirements
Must have
• LARGE FONT, ROUNDED EDGES,
Nice to have
• ON THE BACK SIDE :
• THE HEADLAND AT TALL PINE
• HUDSON RIVER WATERFRONT LAND
• 2 TO 67 ACRES---READY TO BUILD
• PRICED TO SELL!

```html
<!DOCTYPE html>
<html lang="en">
<head>
<meta charset="utf-8">
<title>The Headland at Tall Pine – Business Cards</title>
<link rel="stylesheet" href="https://fonts.googleapis.com/css2?family=Oswald:wght@500;600&display=swap">
<style>
  :root {
    --backdrop: #646866;
    --wood-light: #efdcc0;
    --wood-mid: #e3c9a5;
    --ink: #4a2c1a;
    --mark: #3e403f;
    --card-w: 393px;
    --card-h: 692px;
  }
  html, body {
    margin: 0;
    width: 1200px;
    height: 877px;
    overflow: hidden;
    background: var(--backdrop);
  }
  .sheet {
    position: relative;
    width: 1200px;
    height: 877px;
    font-family: "Oswald", "Arial Narrow", sans-serif;
    color: var(--ink);
  }
  .card {
    position: absolute;
    top: 93px;
    width: var(--card-w);
    height: var(--card-h);
    border-radius: 32px;
    background: linear-gradient(160deg, var(--wood-light) 0%, var(--wood-mid) 100%);
    text-align: center;
  }
  .card--project { left: 164px; }
  .card--contact { left: 645px; }
  .emblem {
    position: absolute;
    left: 40px;
    top: 34px;
    width: 312px;
    height: 360px;
    border-radius: 50% 50% 48% 48%;
    background: var(--mark);
  }
  .line {
    position: absolute;
    left: 0;
    right: 0;
    margin: 0;
    line-height: 1;
    font-weight: 600;
    text-transform: uppercase;
  }
  .project-name   { top: 428px; font-size: 25px; letter-spacing: 0.3px; }
  .project-sub    { top: 460px; font-size: 22px; letter-spacing: 0.3px; }
  .project-point  { font-size: 48px; letter-spacing: 0.5px; }
  .project-point--acres { top: 503px; }
  .project-point--build { top: 558px; }
  .project-point--price { top: 613px; }
  .contact-name   { top: 425px; font-size: 46px; letter-spacing: 1px; }
  .contact-role   { top: 489px; font-size: 24px; font-weight: 500; letter-spacing: 0.5px; }
  .contact-rule {
    position: absolute;
    top: 537px;
    left: 70px;
    right: 70px;
    height: 2px;
    background: linear-gradient(90deg, transparent, var(--ink) 20%, var(--ink) 80%, transparent);
  }
  .contact-phone  { top: 558px; font-size: 48px; letter-spacing: 1px; }
  .contact-email  { top: 622px; font-size: 24px; font-weight: 500; letter-spacing: 0.3px; }
</style>
</head>
<body>
<main class="sheet">
  <section class="card card--project">
    <div class="emblem" role="img" aria-label="River otter silhouette on a rock with a leafy tree, cut into a dark round mark"></div>
    <p class="line project-name">The Headland at Tall Pine</p>
    <p class="line project-sub">Hudson River Waterfront Land</p>
    <p class="line project-point project-point--acres">2 to 67 Acres</p>
    <p class="line project-point project-point--build">Ready to Build</p>
    <p class="line project-point project-point--price">Priced to Sell!</p>
  </section>
  <section class="card card--contact">
    <div class="emblem" role="img" aria-label="River otter silhouette on a rock with a leafy tree, cut into a dark round mark"></div>
    <p class="line contact-name">Martin Kowalczyk</p>
    <p class="line contact-role">Stone Meadow LLC Principal</p>
    <div class="contact-rule"></div>
    <p class="line contact-phone">607-318-5942</p>
    <p class="line contact-email">RQVWFIELD@NORVAMAIL.NET</p>
  </section>
</main>
</body>
</html>
```